Business card design needed

Marketing Communications

Target Market(s)

prospective clients in the marketing communications industry

Industry/Entity Type

Business

Contact Information for Business Card

marel tusk
Marketing Communications
lorapen@tidewire.com
0493 518274

Logo Text

marel tusk

Logo styles of interest
Abstract Logo
Requirements
Must have
• An appropriate abstract logo. only a one or two colour design
Nice to have
• Logo to portray the growth of a marketing brief
Should not have
• no more than two colours maximum

```html
<!DOCTYPE html>
<html lang="en">
<head>
<meta charset="utf-8">
<title>Marel Tusk – Business Card</title>
<link rel="stylesheet" href="https://fonts.googleapis.com/css2?family=Bodoni+Moda:ital,opsz,wght@0,6..96,400;1,6..96,400&display=swap">
<style>
  :root {
    --card-sand: #dfca98;
    --accent-gold: #cdad5e;
    --ink-navy: #0e1240;
  }
  html, body {
    margin: 0;
    padding: 0;
    width: 1200px;
    height: 695px;
    overflow: hidden;
    background: var(--card-sand);
  }
  .card {
    display: block;
    width: 1200px;
    height: 695px;
  }
  .card-bg { fill: var(--card-sand); }
  .brand-square { fill: var(--accent-gold); }
  .rule { stroke: var(--ink-navy); stroke-width: 1.2; }
  .name {
    font-family: "Bodoni Moda", "Didot", serif;
    font-weight: 400;
    font-size: 178px;
    fill: var(--ink-navy);
  }
  .title {
    font-family: "Bodoni Moda", "Didot", serif;
    font-weight: 400;
    font-size: 54px;
    fill: var(--ink-navy);
  }
  .contact {
    font-family: "Bodoni Moda", "Didot", serif;
    font-style: italic;
    font-weight: 400;
    font-size: 66px;
    fill: var(--ink-navy);
  }
</style>
</head>
<body>
<svg class="card" viewBox="0 0 1200 695" xmlns="http://www.w3.org/2000/svg" aria-label="Marel Tusk business card">
  <rect class="card-bg" x="0" y="0" width="1200" height="695"/>
  <rect class="brand-square" x="0" y="0" width="132" height="189"/>

  <text class="name" x="147" y="181" textLength="1013" lengthAdjust="spacingAndGlyphs">Marel Tusk</text>
  <text class="title" x="68" y="240">marketing communications</text>
  <line class="rule" x1="806" y1="240" x2="1200" y2="240"/>

  <line class="rule" x1="0" y1="419" x2="453" y2="419"/>
  <text class="contact" x="1183" y="419" text-anchor="end">lorapen@tidewire.com</text>

  <line class="rule" x1="0" y1="559" x2="815" y2="559"/>
  <text class="contact" x="1172" y="563" text-anchor="end">0493 518274</text>
</svg>
</body>
</html>
```